Kindlemoor Critters Florida Retractable Banner Design

Looking for a fresh, modern, eye catching yet informative retractable banner design for our vendor booth events.

Our color scheme is teal, dark yellow, black, and white

Would like to include our services of Overnights, Pop in Visits, Dog Walking, Transport, and Attendants. We are veterinary professionals that offer a higher tier level of pet care.

Our tagline is Setting the Standard in Professional Pet Care

Require logo to be incorporated

Would like our images used or included

Would like to include that we offer law enforcement and military discounts

www.kindlemoorcritters.net is our website
An example of our print marketing materials attached

```html
<!DOCTYPE html>
<html lang="en">
<head>
<meta charset="UTF-8">
<title>Kindlemoor Critters Florida – Retractable Banner</title>
<link rel="stylesheet" href="https://fonts.googleapis.com/css2?family=Montserrat:wght@300;400;600;700&display=swap">
<style>
  :root {
    --stage: #f3f3f1;
    --banner-yellow: #fdac17;
    --banner-yellow-deep: #f7a40f;
    --ink: #141414;
    --white: #ffffff;
    --teal: #3ecfcb;
    --fur-grey: #8d8b86;
    --fur-light: #d9d6cf;
  }
  * { margin: 0; padding: 0; box-sizing: border-box; }
  html, body {
    width: 1200px;
    height: 841px;
    overflow: hidden;
    background: var(--stage);
    font-family: "Montserrat", sans-serif;
  }
  .banner {
    position: absolute;
    left: 441px;
    top: 25px;
    width: 318px;
    height: 790px;
    background: linear-gradient(180deg, var(--banner-yellow) 0%, var(--banner-yellow-deep) 100%);
    overflow: hidden;
    color: var(--ink);
  }
  .photo { position: absolute; }
  .photo--kitten {
    left: 0; top: 0;
    width: 200px; height: 262px;
    background: radial-gradient(ellipse at 35% 45%, var(--fur-light) 0%, var(--fur-grey) 55%, rgba(253,172,23,0) 100%);
    border-bottom-right-radius: 60px;
  }
  .photo--dog {
    left: 135px; top: 505px;
    width: 183px; height: 285px;
    background: radial-gradient(ellipse at 60% 55%, var(--fur-light) 0%, var(--fur-grey) 60%, rgba(253,172,23,0) 100%);
    border-top-left-radius: 90px;
  }
  .brand {
    position: absolute;
    left: 134px; top: 62px;
    width: 200px;
    text-align: center;
    font-weight: 600;
    font-size: 11px;
    line-height: 1.35;
    letter-spacing: 0.02em;
    text-transform: uppercase;
    color: var(--ink);
  }
  .brand__dot {
    display: block;
    width: 40px; height: 40px;
    margin: 0 auto 10px;
    border-radius: 50%;
    background: var(--ink);
  }
  .rule {
    position: absolute;
    height: 1px;
    background: var(--ink);
    opacity: 0.55;
  }
  .rule--a1 { left: 0; top: 304px; width: 58px; }
  .rule--a2 { left: 163px; top: 304px; width: 155px; }
  .rule--b  { left: 240px; top: 332px; width: 78px; }
  .rule--c  { left: 0; top: 365px; width: 61px; }
  .headline {
    position: absolute;
    font-weight: 300;
    font-size: 29px;
    line-height: 1;
    letter-spacing: -0.01em;
    white-space: nowrap;
  }
  .headline--we   { left: 57px; top: 283px; }
  .headline--vet  { left: 83px; top: 309px; }
  .headline--pro  { left: 61px; top: 339px; }
  .intro {
    position: absolute;
    left: 61px; top: 374px;
    font-size: 10.5px;
    line-height: 1.65;
  }
  .intro strong { font-weight: 700; }
  .services {
    position: absolute;
    left: 61px; top: 424px;
    font-size: 10.5px;
    line-height: 1.72;
  }
  .services__title { font-weight: 700; color: var(--white); font-size: 11px; }
  .contact {
    position: absolute;
    left: 24px; top: 659px;
    color: var(--white);
    font-weight: 700;
    font-size: 11.5px;
    line-height: 1.6;
    list-style: none;
  }
  .contact__item { display: flex; align-items: center; gap: 6px; }
  .contact__icon { width: 9px; height: 9px; flex: none; }
</style>
</head>
<body>
  <main class="banner">
    <div class="photo photo--kitten" role="img" aria-label="Photo of a grey tabby kitten reaching forward with one paw"></div>

    <div class="brand">
      <span class="brand__dot"></span>
      Kindlemoor Critters<br>Florida
    </div>

    <span class="rule rule--a1"></span>
    <span class="rule rule--a2"></span>
    <span class="rule rule--b"></span>
    <span class="rule rule--c"></span>

    <h1>
      <span class="headline headline--we">We are</span>
      <span class="headline headline--vet">Veterinary</span>
      <span class="headline headline--pro">Professionals</span>
    </h1>

    <p class="intro"><strong>that offer a higher tier level</strong><br>of pet care.</p>

    <div class="services">
      <p class="services__title">Our services are</p>
      <p>Overnights, Pop in Visits,<br>Dog Walking, Transport,<br>and Attendants.</p>
    </div>

    <div class="photo photo--dog" role="img" aria-label="Photo of a grey and white dog wearing round yellow-tinted glasses, looking up"></div>

    <ul class="contact">
      <li class="contact__item">
        <svg class="contact__icon" viewBox="0 0 20 20" aria-hidden="true">
          <g fill="none" stroke="#141414" stroke-width="1.8">
            <circle cx="10" cy="10" r="8.5"/>
            <ellipse cx="10" cy="10" rx="3.8" ry="8.5"/>
            <path d="M1.5 10h17M3 5.5h14M3 14.5h14"/>
          </g>
        </svg>
        www.kindlemoorcritters.net
      </li>
      <li class="contact__item">
        <svg class="contact__icon" viewBox="0 0 20 20" aria-hidden="true">
          <path fill="#141414" d="M4.2 1.5l3 3.3-1.6 2.3c1 2.4 3 4.4 5.4 5.4l2.3-1.6 3.3 3-1.5 3c-7.7-.5-13.4-6.2-14-13.9z"/>
        </svg>
        +1 555-014-2273
      </li>
    </ul>
  </main>
</body>
</html>
```